Design Large Inspirational Artwork with Long Quote

Design a large piece of art with a quote from Marcus Tillwright.

QUOTE
"The thing that's so interesting about being alive is that you're all in. No matter what you do, you're all in. This is gonna kill you, so I think you might as well play the most magnificent game you can while you're waiting. Because, do you have anything better to do? Why not pick the best thing possible that you could do? Because you're more powerful than you think, way more powerful than you think. I mean, God only knows what you are in the final analysis. You're blind to your own weaknesses, but you're also blind to your own strengths. How far could you take that if you stopped wasting time, and if you stopped lying, and if you oriented yourself to the highest possible good that you could conceive of and you committed to that? How much good could you do? Well, I would say: why don't you find out?"

SIZE
A high-resolution print size of 6' wide and 3' tall should provide ample space for both the quote and the accompanying artwork.

TYPOGRAPHY
Choose a bold, clean, and easily readable font for the quote. You could also experiment with different font sizes for certain words or phrases to emphasize their importance within the quote.

COLORS
Since the quote is thought-provoking and reflective, you might want to use a color palette that evokes a sense of introspection and depth. Consider using cool, calming colors like shades of blue, gray, or green. Alternatively, you can use a contrasting color scheme with a light background and dark text to make the quote stand out.

ARTWORK
Select / create / edit background artwork to complement the quote.
While a great design might be minimalistic and/or greyscale, I'd really like to see some full color options. This might be anything from photography or graphics inspired by the ideas in the text, to abstract colors or illustrations that feel like the sentiment expressed.
The art should capture your attention and encourage you to read the text. The art should be visually appealing, both at a distance and up close, regardless of whether the text is read.
Updates

Having trouble confirming the exact print size.

Still looking for printing solution and final size confirmation.

Target Market(s)

Personal, business, office

Industry/Entity Type

None

Font styles to use
Sans Serif
Script

Requirements
Must have
• Entire quote, legible text, modern design, attractive artwork, approx 6ft wide and 3ft tall
Nice to have
• Different font (sizes) for certain words or phrases to emphasize their importance within the quote.

```html
<!DOCTYPE html>
<html lang="en">
<head>
<meta charset="utf-8">
<title>Why Don't You Find Out – Quote Artwork</title>
<link rel="stylesheet" href="https://fonts.googleapis.com/css2?family=Montserrat:wght@500;600;700;800&display=swap">
<style>
  :root {
    --navy-deep: #041a30;
    --navy: #07304f;
    --ocean: #0d5a86;
    --glow: #3fa3d1;
    --text: #ffffff;
    --label-bg: rgba(150, 192, 232, 0.6);
  }
  html, body {
    margin: 0;
    padding: 0;
    overflow: hidden;
    background: var(--navy-deep);
  }
  .artwork {
    position: relative;
    width: 1200px;
    height: 600px;
    overflow: hidden;
    font-family: "Montserrat", sans-serif;
    color: var(--text);
  }
  .artwork__background {
    position: absolute;
    inset: 0;
    background:
      radial-gradient(circle at 90% 18%, rgba(90, 200, 235, 0.55) 0, rgba(63, 163, 209, 0.2) 12%, transparent 30%),
      radial-gradient(ellipse at 15% 75%, rgba(63, 163, 209, 0.45) 0, transparent 40%),
      radial-gradient(ellipse at 55% 45%, rgba(13, 90, 134, 0.6) 0, transparent 55%),
      radial-gradient(ellipse at 80% 80%, rgba(13, 90, 134, 0.7) 0, transparent 45%),
      linear-gradient(135deg, var(--navy) 0%, var(--navy-deep) 45%, var(--ocean) 100%);
  }
  .quote {
    position: absolute;
    inset: 0;
    margin: 0;
  }
  .quote__line {
    position: absolute;
    transform: translateY(-50%);
    white-space: nowrap;
    font-size: 12px;
    font-weight: 600;
    font-variant: small-caps;
    letter-spacing: 0.05em;
    line-height: 1;
    text-shadow: 0 1px 4px rgba(0, 20, 40, 0.5);
  }
  .em {
    font-size: 19px;
    font-weight: 700;
    font-variant: normal;
    text-transform: uppercase;
    letter-spacing: 0.04em;
  }
  .em--god { font-size: 30px; }
  .em--finale { font-size: 30px; font-weight: 800; letter-spacing: 0.05em; }
  .attribution {
    position: absolute;
    left: 913px;
    top: 509px;
    width: 217px;
    height: 35px;
    background: var(--label-bg);
    display: flex;
    align-items: center;
    justify-content: center;
    font-size: 18px;
    font-weight: 700;
    letter-spacing: 0.01em;
    margin: 0;
  }
</style>
</head>
<body>
<main class="artwork">
  <div class="artwork__background" role="img" aria-label="Abstract deep blue background of flowing translucent swirls and glowing bubbles"></div>

  <blockquote class="quote">
    <div class="quote__line" style="left:150px; top:50px;">"The thing that's so <span class="em">interesting</span> about being <span class="em">alive</span> is that you're all in.</div>
    <div class="quote__line" style="left:224px; top:71px;">no <span class="em">matter</span> what you <span class="em">do</span>, you're <span class="em">all in</span>.</div>
    <div class="quote__line" style="left:438px; top:94px;">this is gonna <span class="em">kill you</span>,</div>
    <div class="quote__line" style="left:224px; top:122px;">So i think you might as <span class="em">well play</span> the most <span class="em">magnificent game</span></div>
    <div class="quote__line" style="left:528px; top:146px;">you can while you're <span class="em">waiting</span>.</div>
    <div class="quote__line" style="left:387px; top:167px;">because, do you have anything <span class="em">better</span> to do?</div>
    <div class="quote__line" style="left:302px; top:195px;">Why not pick <span class="em">the best</span> thing <span class="em">possible</span> that you could do?</div>
    <div class="quote__line" style="left:456px; top:221px;">because you're more <span class="em">powerful</span> than you think,</div>
    <div class="quote__line" style="left:589px; top:246px;">way more <span class="em">powerful</span> than you think.</div>
    <div class="quote__line" style="left:250px; top:272px;">I mean, <span class="em em--god">God</span> only knows what you are in <span class="em">the final analysis</span>.</div>
    <div class="quote__line" style="left:506px; top:297px;">you're <span class="em">blind</span> to your own <span class="em">weaknesses</span>,</div>
    <div class="quote__line" style="left:474px; top:319px;">but you're also <span class="em">blind</span> to your own <span class="em">strength</span></div>
    <div class="quote__line" style="left:306px; top:348px;">How far could you take that if you <span class="em">stopped wasting time</span>,</div>
    <div class="quote__line" style="left:470px; top:373px;">and if you <span class="em">stopped lying</span>,</div>
    <div class="quote__line" style="left:522px; top:397px;">and if you <span class="em">oriented yourself</span></div>
    <div class="quote__line" style="left:552px; top:422px;">to <span class="em">the highest possible good</span></div>
    <div class="quote__line" style="left:262px; top:452px;">that you could <span class="em">conceive</span> of and you <span class="em">committed</span> to that?</div>
    <div class="quote__line" style="left:400px; top:476px;">how much <span class="em">good</span> could you do?</div>
    <div class="quote__line" style="left:502px; top:504px;">well, i would say:</div>
    <div class="quote__line" style="left:318px; top:528px;"><span class="em em--finale">Why don't you find out?"</span></div>
  </blockquote>

  <p class="attribution">Marcus Tillwright</p>
</main>
</body>
</html>
```